Business Card Design Project

Business card design with a funky, clean, modern design. Business is an immigration consultancy. Client base will be Canadian employers wanting to hire or retain foreign workers and foreign nationals wanting to immigrate to Canada.

Full color possible, but should incorporate red/white/black as per the logo to be provided. Double sided card design.

Target Market(s)

Canadian employers looking to hire/retain staff and also foreign nationals immigrating to Canada

Industry/Entity Type

Business

Requirements
Must have
• Logo (to be provided)
Name (Marla Quintero, Immigration Consultant)
Phone (604) 517-3362
E-mail: marla@lanternpathvisas.example
Web: www.lanternpathvisas.example

Nice to have
• Tag Line
Clean, modern style

```html
<!DOCTYPE html>
<html lang="en">
<head>
<meta charset="utf-8">
<title>Lanternpath Visas – Business Card</title>
<link href="https://fonts.googleapis.com/css2?family=Open+Sans:wght@400;700&display=swap" rel="stylesheet">
<style>
  :root {
    --bg: #d9d6d2;
    --card-dark: #2b2526;
    --brand-red: #d4202a;
    --white: #ffffff;
    --light: #f1f1f1;
    --text-light: #f4f4f4;
  }
  html, body {
    margin: 0;
    padding: 0;
    width: 1200px;
    height: 951px;
    overflow: hidden;
    background: var(--bg);
    font-family: "Open Sans", sans-serif;
  }
  .canvas {
    position: relative;
    width: 1200px;
    height: 951px;
  }
  .card {
    position: absolute;
    width: 580px;
    height: 340px;
    border-radius: 18px;
    overflow: hidden;
    box-shadow: 0 10px 28px rgba(0,0,0,0.28);
  }

  /* Front */
  .card-front {
    left: 70px;
    top: 110px;
    background: var(--card-dark);
  }
  .card-front .edge {
    position: absolute;
    top: 0;
    bottom: 0;
    width: 12px;
    background: var(--brand-red);
  }
  .card-front .edge-left { left: 0; }
  .card-front .edge-right { right: 0; }
  .card-front .brand {
    position: absolute;
    left: 0;
    right: 0;
    top: 62px;
    text-align: center;
  }
  .brand-mark {
    display: block;
    width: 62px;
    height: 62px;
    margin: 0 auto 14px;
    border-radius: 50%;
    background: var(--brand-red);
  }
  .brand-name {
    margin: 0;
    font-weight: 700;
    font-size: 30px;
    line-height: 1.1;
    letter-spacing: 1px;
    color: var(--white);
    text-transform: uppercase;
  }
  .card-front .tagline {
    position: absolute;
    left: 0;
    right: 0;
    bottom: 48px;
    margin: 0;
    text-align: center;
    font-size: 17px;
    color: var(--text-light);
  }

  /* Back */
  .card-back {
    left: 550px;
    top: 470px;
    background: var(--card-dark);
  }
  .card-back .top {
    position: absolute;
    left: 0;
    right: 0;
    top: 0;
    height: 140px;
    background: linear-gradient(#ffffff, var(--light));
    border-bottom: 8px solid var(--brand-red);
  }
  .card-back .brand {
    position: absolute;
    left: 0;
    right: 0;
    top: 22px;
    text-align: center;
  }
  .card-back .brand-mark {
    width: 44px;
    height: 44px;
    margin-bottom: 8px;
  }
  .card-back .brand-name {
    font-size: 22px;
    color: var(--card-dark);
  }
  .contact {
    position: absolute;
    left: 0;
    right: 0;
    top: 166px;
    text-align: center;
    color: var(--text-light);
  }
  .contact-name {
    margin: 0 0 8px;
    font-size: 22px;
    font-weight: 400;
  }
  .credential {
    font-size: 14px;
    color: var(--brand-red);
  }
  .contact-line {
    margin: 0;
    font-size: 15px;
    line-height: 1.5;
  }
  .accent { color: var(--brand-red); }
</style>
</head>
<body>
<main class="canvas">
  <section class="card card-front" aria-label="Card front">
    <span class="edge edge-left"></span>
    <span class="edge edge-right"></span>
    <div class="brand">
      <span class="brand-mark"></span>
      <p class="brand-name">Lanternpath Visas</p>
    </div>
    <p class="tagline">Clear pathways. Confident moves. Brighter futures ahead today.</p>
  </section>

  <section class="card card-back" aria-label="Card back">
    <div class="top">
      <div class="brand">
        <span class="brand-mark"></span>
        <p class="brand-name">Lanternpath Visas</p>
      </div>
    </div>
    <div class="contact">
      <h1 class="contact-name">Marla Quintero <span class="credential">RCIC</span></h1>
      <p class="contact-line">Phone: (604) 517-3362</p>
      <p class="contact-line">marla@lanternpathvisas.example</p>
      <p class="contact-line">www.<span class="accent">lanternpathvisas</span>.example</p>
      <p class="contact-line">Offices in Cedar Hollow, Pine Bay and Westbrook</p>
    </div>
  </section>
</main>
</body>
</html>
```